Need updated stationery design for chiropractic clinic

We recently moved our office and are looking to refresh our letterhead, business cards, presentation folder and envelopes. I tend to prefer simple, clean designs. We communicate with a lot of attorneys and want to exude professionalism. I have attached our logo and 2 additional versions (all white and white letters instead of grey).

Target Market(s)

Other medical professionals and attorneys. Business cards will go to patients as well.

Industry/Entity Type

Healthcare

```html
<!DOCTYPE html>
<html lang="en">
<head>
<meta charset="utf-8">
<title>Vertex Spine Clinic — Stationery Suite</title>
<link href="https://fonts.googleapis.com/css2?family=Montserrat:wght@400;500;600;700&display=swap" rel="stylesheet">
<style>
  :root{
    --stage:#e4e8eb;
    --paper:#ffffff;
    --blue:#0a9bd5;
    --blue-deep:#0288c7;
    --cyan:#1ac6d4;
    --ink:#3f4549;
    --ink-soft:#6b7378;
  }
  *{box-sizing:border-box;margin:0;padding:0}
  html,body{width:1200px;height:3000px;overflow:hidden}
  body{background:var(--stage);font-family:"Montserrat",sans-serif;color:var(--ink);position:relative}
  .piece{position:absolute;overflow:hidden;box-shadow:0 14px 30px rgba(40,60,80,.16)}
  .paper{background:var(--paper)}
  .blue{background:linear-gradient(135deg,var(--blue) 0%,var(--blue-deep) 100%)}

  .brand{display:flex;align-items:center;gap:10px;font-weight:700;color:var(--blue);white-space:nowrap;letter-spacing:-.2px}
  .brand i{display:block;background:currentColor;border-radius:3px}
  .brand.light{color:#fff}

  .contact{list-style:none;color:var(--ink)}
  .contact li{display:flex;align-items:center;gap:7px;line-height:1.55}
  .contact svg{flex:none;fill:var(--blue)}
  .band{position:absolute;left:0;bottom:0;width:100%}
  .band svg{display:block;width:100%;height:100%}

  /* business card */
  .card{width:560px;height:320px;border-radius:18px}
  .card-front{left:320px;top:60px}
  .card-back{left:320px;top:410px}
  .card-front .brand{position:absolute;right:40px;top:52px;font-size:24px}
  .card-front .brand i{width:22px;height:22px}
  .holder{position:absolute;left:48px;top:132px;padding-left:14px;border-left:4px solid var(--blue)}
  .holder-name{font-size:22px;font-weight:700;color:var(--blue);letter-spacing:.3px}
  .holder-role{font-size:13px;font-weight:500;color:var(--ink-soft);letter-spacing:1px;margin-top:2px}
  .card-front .contact{position:absolute;left:48px;top:200px;font-size:11.5px}
  .card-front .contact svg{width:11px;height:11px}
  .card-front .band{height:22px}
  .card-back .brand{position:absolute;left:50%;top:50%;transform:translate(-50%,-50%);font-size:38px;gap:14px}
  .card-back .brand i{width:32px;height:32px}

  /* folder */
  .folder{left:180px;top:800px;width:840px;height:560px;display:flex}
  .folder-back{position:relative;width:50%;height:100%;background:var(--paper);border-right:1px solid #d4dadd}
  .folder-front{position:relative;width:50%;height:100%}
  .folder-back .brand{position:absolute;left:40px;bottom:112px;font-size:22px}
  .folder-back .brand i{width:20px;height:20px}
  .folder-back .cols{position:absolute;left:40px;right:24px;bottom:42px;display:flex;gap:22px}
  .folder-back .contact{font-size:8.5px}
  .folder-back .contact svg{width:8px;height:8px}
  .folder-back .band{height:14px}
  .folder-front .brand{position:absolute;left:50%;top:170px;transform:translateX(-50%);font-size:30px;gap:12px}
  .folder-front .brand i{width:26px;height:26px}

  /* envelopes */
  .env10{width:470px;height:204px}
  .env10-front{left:40px;top:1490px}
  .env10-back{left:40px;top:1730px}
  .env10-front .brand{position:absolute;left:28px;top:26px;font-size:18px;gap:8px}
  .env10-front .brand i{width:16px;height:16px}
  .env10-front .contact{position:absolute;right:34px;bottom:30px;font-size:7.5px}
  .env10-front .contact svg{width:7px;height:7px}
  .env10-front .band{height:10px}
  .env10-back .brand{position:absolute;left:50%;top:118px;transform:translateX(-50%);font-size:22px}
  .env10-back .brand i{width:18px;height:18px}
  .flap-line{position:absolute;inset:0;width:100%;height:100%}

  .catalog{width:300px;height:400px}
  .catalog-front{left:560px;top:1490px}
  .catalog-back{left:880px;top:1490px}
  .catalog-front .flap{position:absolute;left:0;top:0;width:100%;height:46px;background:var(--blue)}
  .catalog-front .brand{position:absolute;left:28px;top:76px;font-size:19px;gap:8px}
  .catalog-front .brand i{width:16px;height:16px}
  .catalog-front .contact{position:absolute;left:28px;bottom:32px;font-size:7.5px}
  .catalog-front .contact svg{width:7px;height:7px}
  .catalog-front .band{height:10px}
  .catalog-back .brand{position:absolute;left:50%;top:200px;transform:translateX(-50%);font-size:22px;gap:8px}
  .catalog-back .brand i{width:18px;height:18px}

  /* letterhead */
  .letterhead{left:250px;top:2010px;width:700px;height:906px}
  .letterhead .brand{position:absolute;right:60px;top:64px;font-size:28px;gap:12px}
  .letterhead .brand i{width:24px;height:24px}
  .letterhead .cols{position:absolute;left:60px;right:60px;bottom:58px;display:flex;gap:60px}
  .letterhead .contact{font-size:10.5px}
  .letterhead .contact svg{width:10px;height:10px}
  .letterhead .band{height:22px}
</style>
</head>
<body>

<svg width="0" height="0" style="position:absolute" aria-hidden="true">
  <defs>
    <symbol id="ico-phone" viewBox="0 0 24 24"><path d="M6.6 10.8a15.1 15.1 0 0 0 6.6 6.6l2.2-2.2a1 1 0 0 1 1-.25 11.4 11.4 0 0 0 3.6.57 1 1 0 0 1 1 1V20a1 1 0 0 1-1 1A17 17 0 0 1 3 4a1 1 0 0 1 1-1h3.5a1 1 0 0 1 1 1c0 1.25.2 2.45.57 3.57a1 1 0 0 1-.25 1z"/></symbol>
    <symbol id="ico-web" viewBox="0 0 24 24"><path d="M12 2a10 10 0 1 0 0 20 10 10 0 0 0 0-20zm6.9 6h-3a15.6 15.6 0 0 0-1.4-3.6A8 8 0 0 1 18.9 8zM12 4c.8 1.2 1.5 2.5 1.9 4h-3.8c.4-1.5 1.1-2.8 1.9-4zM4.3 14a8 8 0 0 1 0-4h3.4a16 16 0 0 0 0 4zm.8 2h3a15.6 15.6 0 0 0 1.4 3.6A8 8 0 0 1 5.1 16zm3-8h-3a8 8 0 0 1 4.4-3.6A15.6 15.6 0 0 0 8.1 8zM12 20c-.8-1.2-1.5-2.5-1.9-4h3.8c-.4 1.5-1.1 2.8-1.9 4zm2.3-6H9.7a14.7 14.7 0 0 1 0-4h4.6a14.7 14.7 0 0 1 0 4zm.3 5.6a15.6 15.6 0 0 0 1.4-3.6h3a8 8 0 0 1-4.4 3.6zm1.7-5.6a16 16 0 0 0 0-4h3.4a8 8 0 0 1 0 4z"/></symbol>
    <symbol id="ico-mail" viewBox="0 0 24 24"><path d="M3 5h18a1 1 0 0 1 1 1v12a1 1 0 0 1-1 1H3a1 1 0 0 1-1-1V6a1 1 0 0 1 1-1zm9 7.2L4.4 7H4v.6l8 5.5 8-5.5V7h-.4z"/></symbol>
    <symbol id="ico-pin" viewBox="0 0 24 24"><path d="M12 2a7 7 0 0 0-7 7c0 5.2 7 13 7 13s7-7.8 7-13a7 7 0 0 0-7-7zm0 9.5A2.5 2.5 0 1 1 12 6.5a2.5 2.5 0 0 1 0 5z"/></symbol>
    <symbol id="band-split" viewBox="0 0 100 10" preserveAspectRatio="none">
      <polygon points="0,0 55,0 53.5,10 0,10" fill="#0288c7"/>
      <polygon points="56,0 100,0 100,10 54.5,10" fill="#1ac6d4"/>
    </symbol>
    <symbol id="band-cyan-first" viewBox="0 0 100 10" preserveAspectRatio="none">
      <polygon points="0,0 42,0 40.5,10 0,10" fill="#1ac6d4"/>
      <polygon points="43,0 100,0 100,10 41.5,10" fill="#0288c7"/>
    </symbol>
  </defs>
</svg>

<!-- Business card: front -->
<section class="piece paper card card-front" aria-label="Business card front">
  <div class="brand"><i></i>Vertex Spine Clinic</div>
  <div class="holder">
    <p class="holder-name">YOUR FULL NAME</p>
    <p class="holder-role">DIRECTOR</p>
  </div>
  <ul class="contact">
    <li><svg><use href="#ico-phone"/></svg>555-210-4400 Fax: 555-210-4401</li>
    <li><svg><use href="#ico-web"/></svg>www.vertexspineclinic.com</li>
    <li><svg><use href="#ico-mail"/></svg>mlane@vertexspineclinic.com</li>
    <li><svg><use href="#ico-pin"/></svg>Mara Lane, D.C. 820 Alder Ave. Suite 210 Riverton, OH 45000</li>
  </ul>
  <div class="band"><svg preserveAspectRatio="none"><use href="#band-split"/></svg></div>
</section>

<!-- Business card: back -->
<section class="piece blue card card-back" aria-label="Business card back">
  <div class="brand light"><i></i>Vertex Spine Clinic</div>
</section>

<!-- Presentation folder: outside spread -->
<section class="piece folder" aria-label="Presentation folder outside">
  <div class="folder-back">
    <div class="brand"><i></i>Vertex Spine Clinic</div>
    <div class="cols">
      <ul class="contact">
        <li><svg><use href="#ico-phone"/></svg>555-210-4400 Fax: 555-210-4401</li>
        <li><svg><use href="#ico-web"/></svg>www.vertexspineclinic.com</li>
      </ul>
      <ul class="contact">
        <li><svg><use href="#ico-mail"/></svg>mlane@vertexspineclinic.com</li>
        <li><svg><use href="#ico-pin"/></svg>Mara Lane, D.C. 820 Alder Ave. Suite 210 Riverton, OH</li>
      </ul>
    </div>
    <div class="band"><svg preserveAspectRatio="none"><use href="#band-cyan-first"/></svg></div>
  </div>
  <div class="folder-front blue">
    <div class="brand light"><i></i>Vertex Spine Clinic</div>
  </div>
</section>

<!-- #10 envelope: front -->
<section class="piece paper env10 env10-front" aria-label="Envelope front">
  <div class="brand"><i></i>Vertex Spine Clinic</div>
  <ul class="contact">
    <li><svg><use href="#ico-phone"/></svg>555-210-4400 Fax: 555-210-4401</li>
    <li><svg><use href="#ico-web"/></svg>www.vertexspineclinic.com</li>
    <li><svg><use href="#ico-mail"/></svg>mlane@vertexspineclinic.com</li>
    <li><svg><use href="#ico-pin"/></svg>820 Alder Ave. Suite 210 Riverton, OH 45000</li>
  </ul>
  <div class="band"><svg preserveAspectRatio="none"><use href="#band-cyan-first"/></svg></div>
</section>

<!-- #10 envelope: back -->
<section class="piece blue env10 env10-back" aria-label="Envelope back">
  <svg class="flap-line" viewBox="0 0 470 204" preserveAspectRatio="none" aria-hidden="true">
    <polyline points="0,0 235,92 470,0" fill="none" stroke="rgba(255,255,255,.28)" stroke-width="1.5"/>
  </svg>
  <div class="brand light"><i></i>Vertex Spine Clinic</div>
</section>

<!-- Catalog envelope: front -->
<section class="piece paper catalog catalog-front" aria-label="Catalog envelope front">
  <div class="flap"></div>
  <div class="brand"><i></i>Vertex Spine Clinic</div>
  <ul class="contact">
    <li><svg><use href="#ico-phone"/></svg>555-210-4400 Fax: 555-210-4401</li>
    <li><svg><use href="#ico-web"/></svg>www.vertexspineclinic.com</li>
    <li><svg><use href="#ico-mail"/></svg>mlane@vertexspineclinic.com</li>
    <li><svg><use href="#ico-pin"/></svg>820 Alder Ave. Suite 210 Riverton, OH 45000</li>
  </ul>
  <div class="band"><svg preserveAspectRatio="none"><use href="#band-cyan-first"/></svg></div>
</section>

<!-- Catalog envelope: back -->
<section class="piece blue catalog catalog-back" aria-label="Catalog envelope back">
  <div class="brand light"><i></i>Vertex Spine Clinic</div>
</section>

<!-- Letterhead -->
<section class="piece paper letterhead" aria-label="Letterhead">
  <div class="brand"><i></i>Vertex Spine Clinic</div>
  <div class="cols">
    <ul class="contact">
      <li><svg><use href="#ico-phone"/></svg>555-210-4400 Fax: 555-210-4401</li>
      <li><svg><use href="#ico-web"/></svg>www.vertexspineclinic.com</li>
    </ul>
    <ul class="contact">
      <li><svg><use href="#ico-mail"/></svg>mlane@vertexspineclinic.com</li>
      <li><svg><use href="#ico-pin"/></svg>Mara Lane, D.C. 820 Alder Ave. Suite 210 Riverton, OH 45000</li>
    </ul>
  </div>
  <div class="band"><svg preserveAspectRatio="none"><use href="#band-cyan-first"/></svg></div>
</section>

</body>
</html>
```